Business Card Design for Law firm - already have logo

Now that we have a logo, we need a business card design - our logo is attached -it is salaryman font if that helps - we would like a file that can be uploaded to cardquill (www.cardquill-example.com) using the logo and with the following information on it:
Quenby Law Firm, P.C.
Delwyn Quenby, Esq.
5817 SW 19th Ave.
Fernhaven, OR 97555
971.555.0142 phone
971.555.0187 fax
del@quenby-example.net
Voxcall: delquenby
Relaytalk: delwyn.quenby@mailbox-example.com
Target Market(s)
our business cards are distributed to corporate executives, technology professionals and healthcare providers
Industry/Entity Type
Business
Look and feel

```html
<!DOCTYPE html>
<html lang="en">
<head>
<meta charset="utf-8">
<title>Quenby Law Firm – Business Card</title>
<link rel="stylesheet" href="https://fonts.googleapis.com/css2?family=Anton&display=swap">
<style>
  :root {
    --blush: #f7c7bf;
    --blush-deep: #c9928b;
    --ink: #111111;
    --frame: #1c1c1c;
    --paper: #ffffff;
    --signal-red: #ee2211;
  }
  html, body {
    margin: 0;
    padding: 0;
    width: 1200px;
    height: 776px;
    overflow: hidden;
    background: var(--paper);
  }
  .card {
    position: relative;
    width: 1200px;
    height: 776px;
    font-family: "Anton", "Arial Narrow", sans-serif;
    font-weight: 400;
    color: var(--ink);
    text-transform: uppercase;
  }
  .pattern-field {
    position: absolute;
    inset: 0;
    background: linear-gradient(135deg, var(--blush) 0%, var(--blush-deep) 50%, var(--blush) 100%);
  }
  .frame-band {
    position: absolute;
    left: 25px;
    top: 28px;
    width: 1140px;
    height: 717px;
    background: var(--frame);
  }
  .face {
    position: absolute;
    left: 68px;
    top: 65px;
    width: 1050px;
    height: 641px;
    background: var(--paper);
  }
  .contact-list {
    position: absolute;
    left: 0;
    top: 0;
    width: 545px;
    margin: 0;
    padding: 0;
    list-style: none;
  }
  .contact-item {
    position: absolute;
    right: 0;
    white-space: nowrap;
    font-size: 33px;
    line-height: 1;
    letter-spacing: 0.3px;
  }
  .contact-item--long { font-size: 30px; letter-spacing: 0; }
  .divider {
    position: absolute;
    left: 591px;
    top: 97px;
    width: 4px;
    height: 537px;
    background: var(--ink);
  }
  .wordmark {
    position: absolute;
    left: 663px;
    top: 228px;
    display: flex;
    align-items: center;
    gap: 18px;
  }
  .wordmark-square {
    width: 88px;
    height: 88px;
    background: var(--ink);
  }
  .wordmark-name {
    font-size: 76px;
    line-height: 1;
    letter-spacing: 13px;
    color: var(--ink);
  }
  .identity {
    position: absolute;
    left: 663px;
    top: 362px;
    font-size: 33px;
    line-height: 1;
  }
  .identity-name {
    display: inline-block;
    color: var(--signal-red);
    padding-bottom: 3px;
    border-bottom: 3px solid var(--signal-red);
    margin-bottom: 14px;
  }
  .identity-line { display: block; margin-bottom: 16px; }
</style>
</head>
<body>
  <div class="card">
    <div class="pattern-field" role="img" aria-label="Repeating tilted pattern of the firm's name tiles on blush pink"></div>
    <div class="frame-band"></div>
    <div class="face"></div>

    <ul class="contact-list">
      <li class="contact-item" style="top:127px;right:8px;">del@quenby-example.net</li>
      <li class="contact-item" style="top:227px;">Voxcall: delquenby</li>
      <li class="contact-item" style="top:327px;">Relaytalk:</li>
      <li class="contact-item contact-item--long" style="top:378px;">delwyn.quenby@mailbox-example.com</li>
      <li class="contact-item" style="top:475px;">971.555.0142 phone</li>
      <li class="contact-item" style="top:576px;">971.555.0187 fax</li>
    </ul>

    <div class="divider"></div>

    <div class="wordmark">
      <span class="wordmark-square"></span>
      <span class="wordmark-name">Quenby</span>
    </div>

    <div class="identity">
      <span class="identity-name">Delwyn Quenby, Esq.</span>
      <span class="identity-line">5817 SW 19th Ave.</span>
      <span class="identity-line">Fernhaven, OR 97555</span>
    </div>
  </div>
</body>
</html>
```